Sign Advertisment for Condominium Development

I need a sign created that will be placed in front of a building that is being converted into a luxury condominium development.

The sign needs to say:

Two, Boutique Luxury Condominiums Delivering late 2015.

Luxury Finishes // Designer Kitchens and Bath // Each Unit over 2,000 Square Feet

Deeded Parking Included with Each Unit

To Learn More, Contact:

Loretta Pinwell or Morgan Tesh
(202) 555-0147
Loretta.Pinwell@nrg-example.com

I need a small disclaimer at the bottom stating:

These Condominium(s) have not been registered by the Office of Residential Property Oversight Bureau of Dwelling Registration Tenancy Transfer and Purchase Section. A Condominium Unit may be reserved on a non-binding reservation agreement, but no contract of sale or lease that is binding on the purchaser may be entered into prior to registration.

Target Market(s)

Young professionals seeking luxury condominium

Industry/Entity Type

Building

Font styles to use
Serif

Colors
00a88f
ffffff

```html
<!DOCTYPE html>
<html lang="en">
<head>
<meta charset="UTF-8">
<title>Boutique Luxury Condominiums Sign</title>
<link rel="stylesheet" href="https://fonts.googleapis.com/css2?family=Bree+Serif&family=Source+Sans+3:wght@300;400;600&display=swap">
<style>
  :root {
    --frame: #000000;
    --teal: #00a88f;
    --white: #ffffff;
  }
  * { margin: 0; padding: 0; box-sizing: border-box; }
  html, body {
    width: 1200px;
    height: 800px;
    overflow: hidden;
    background: var(--frame);
  }
  .sign {
    position: relative;
    width: 1200px;
    height: 800px;
    background: var(--frame);
    padding: 22px;
  }
  .panel {
    position: relative;
    width: 100%;
    height: 100%;
    background: var(--teal);
    color: var(--white);
  }
  .headline {
    position: absolute;
    top: 70px;
    left: 0;
    width: 100%;
    text-align: center;
    font-family: "Bree Serif", Georgia, serif;
    font-size: 50px;
    line-height: 54px;
    letter-spacing: 0.3px;
  }
  .headline .count { font-size: 74px; vertical-align: -4px; }
  .features {
    position: absolute;
    top: 256px;
    left: 100px;
    list-style: none;
    font-family: "Source Sans 3", Arial, sans-serif;
    font-weight: 600;
    font-size: 27px;
    line-height: 39px;
  }
  .contact {
    position: absolute;
    top: 470px;
    left: 98px;
    font-family: "Source Sans 3", Arial, sans-serif;
    font-size: 24px;
  }
  .contact-lead {
    font-weight: 300;
    font-size: 23px;
    margin-left: 56px;
    margin-bottom: 14px;
  }
  .contact-row {
    display: flex;
    align-items: center;
    height: 40px;
  }
  .contact-row svg { width: 34px; height: 28px; margin-right: 22px; flex: none; }
  .contact-row strong { font-weight: 600; }
  .contact-row .joiner { font-weight: 300; margin: 0 7px; }
  .partners {
    position: absolute;
    top: 448px;
    left: 822px;
    width: 250px;
    text-align: center;
    font-family: "Bree Serif", Georgia, serif;
  }
  .partner {
    display: flex;
    align-items: center;
    justify-content: center;
    gap: 10px;
    font-size: 20px;
    line-height: 24px;
    margin-bottom: 30px;
  }
  .partner-mark {
    width: 18px;
    height: 18px;
    background: var(--white);
    flex: none;
  }
  .partner-mark.round { border-radius: 50%; }
  .disclaimer {
    position: absolute;
    left: 40px;
    right: 40px;
    top: 666px;
    text-align: center;
    font-family: "Source Sans 3", Arial, sans-serif;
    font-weight: 400;
    font-size: 17px;
    line-height: 24px;
  }
</style>
</head>
<body>
<main class="sign">
  <section class="panel">
    <h1 class="headline">
      <span class="count">2</span> Boutique Luxury Condominiums<br>Delivering late 2015.
    </h1>

    <ul class="features">
      <li>Luxury Finishes</li>
      <li>Designer Kitchens and Bath</li>
      <li>Each Unit over 2,000 Square Feet</li>
      <li>Deeded Parking Included with Each Unit</li>
    </ul>

    <div class="contact">
      <p class="contact-lead">To Learn More, Contact:</p>
      <p class="contact-row">
        <svg viewBox="0 0 34 28" aria-hidden="true">
          <circle cx="17" cy="8" r="7" fill="#ffffff"/>
          <path d="M3 27 C3 18 9 16 17 16 C25 16 31 18 31 27 Z" fill="#ffffff"/>
        </svg>
        <strong>Loretta Pinwell</strong><span class="joiner">or</span><strong>Morgan Tesh</strong>
      </p>
      <p class="contact-row">
        <svg viewBox="0 0 34 28" aria-hidden="true">
          <path d="M10 2 L14 8 L11 11 C13 16 16 19 20 21 L23 18 L29 22 L26 27 C16 27 6 17 6 5 Z" fill="none" stroke="#ffffff" stroke-width="2" stroke-linejoin="round"/>
        </svg>
        <span>(202) 555-0147</span>
      </p>
      <p class="contact-row">
        <svg viewBox="0 0 34 28" aria-hidden="true">
          <rect x="2" y="5" width="30" height="19" fill="#ffffff"/>
          <path d="M2 5 L17 16 L32 5" fill="none" stroke="#00a88f" stroke-width="2"/>
        </svg>
        <span>Loretta.Pinwell@nrg-example.com</span>
      </p>
    </div>

    <div class="partners">
      <p class="partner"><span class="partner-mark"></span>Northridge Realty Group, LLC</p>
      <p class="partner">Halvers Construction</p>
      <p class="partner"><span class="partner-mark round"></span>Cobaltline Bank</p>
    </div>

    <p class="disclaimer">These Condominium(s) have not been registered by the Office of Residential Property Oversight Bureau of Dwelling Registration Tenancy Transfer and Purchase Section. A Condominium Unit may be reserved on a non-binding reservation agreement, but no contract of sale or lease that is binding on the purchaser may be entered into prior to registration.</p>
  </section>
</main>
</body>
</html>
```